VERIDAX Need a luxury modern business card designed.

Need a luxury modern business card designed. refer to the uploaded files for the company name and logo in the zip file under source files. i will making my descion on monday. so please send in before then so if we need to edit we will have the time. we have a trade show coming up and im on a deadline for printer.

Target Market(s)

high end clients

Contact Information for Business Card

Company nAme and logo. Calvin Ostrow Co-Founder / Project Manager Office # 416-555-0193 Cell # 416-555-0147 VERIDAX.CA Calvin@veridax.ca

Font styles to use
Other font styles liked:
• Modern

Requirements
Must have
• Company name and logo, contact info, using the black, gold and white color scheme.

```html
<!DOCTYPE html>
<html lang="en">
<head>
<meta charset="UTF-8">
<title>VERIDAX Business Card</title>
<link href="https://fonts.googleapis.com/css2?family=Josefin+Sans:wght@300;400&family=Rubik:wght@400;600&display=swap" rel="stylesheet">
<style>
  :root {
    --bg: #cfcfcf;
    --card: #2c2c2c;
    --gold: #9c8c57;
    --white: #f4f4f2;
    --text: #e6e6e6;
  }
  * { margin: 0; padding: 0; box-sizing: border-box; }
  html, body { width: 1200px; height: 1021px; overflow: hidden; }
  body { background: var(--bg); position: relative; font-family: "Rubik", sans-serif; }

  .card {
    position: absolute;
    width: 820px; height: 469px;
    background: var(--card);
    box-shadow: 0 10px 28px rgba(0,0,0,.35);
    overflow: hidden;
  }
  .card--back  { left: 320px; top: 30px; }
  .card--front { left: 60px;  top: 522px; }

  .card__bands { position: absolute; inset: 0; }

  .brand { position: absolute; color: var(--white); }
  .brand__name {
    display: flex; align-items: center; gap: 18px;
    font-family: "Josefin Sans", sans-serif; font-weight: 300;
    letter-spacing: .22em; line-height: 1;
  }
  .brand__mark { width: 14px; height: 14px; background: var(--gold); flex: none; }
  .brand__tagline {
    font-family: "Josefin Sans", sans-serif; font-weight: 400;
    letter-spacing: .34em; text-transform: uppercase; margin-top: 10px;
  }
  .card--back .brand { left: 400px; top: 195px; }
  .card--back .brand__name { font-size: 54px; }
  .card--back .brand__tagline { font-size: 15px; padding-left: 34px; }
  .card--front .brand { left: 60px; top: 62px; }
  .card--front .brand__name { font-size: 40px; }
  .card--front .brand__tagline { font-size: 12px; padding-left: 32px; }

  .person { position: absolute; left: 60px; top: 172px; width: 430px; }
  .person__name { color: var(--gold); font-weight: 600; font-size: 25px; }
  .person__role { color: var(--text); font-size: 19px; margin-top: 4px; }
  .person__rule { height: 1.5px; background: var(--gold); margin: 16px 0 18px; }

  .contacts { display: flex; gap: 50px; }
  .contacts__col { display: flex; flex-direction: column; gap: 6px; }
  .contact { display: flex; align-items: center; gap: 10px; color: var(--text); font-size: 18px; }
  .contact svg { width: 16px; height: 16px; flex: none; }
</style>
</head>
<body>

  <section class="card card--back" aria-label="Card back">
    <svg class="card__bands" viewBox="0 0 820 469" aria-hidden="true">
      <polygon points="0,60 60,0 80,0 0,80" fill="var(--gold)"/>
      <polygon points="0,300 280,170 280,190 0,320" fill="var(--gold)"/>
      <polygon points="40,240 220,160 220,182 40,262" fill="var(--white)"/>
    </svg>
    <div class="brand">
      <div class="brand__name"><span class="brand__mark"></span>VERIDAX</div>
      <div class="brand__tagline">Luxury Landscapes</div>
    </div>
  </section>

  <section class="card card--front" aria-label="Card front">
    <svg class="card__bands" viewBox="0 0 820 469" aria-hidden="true">
      <polygon points="560,469 820,250 820,276 591,469" fill="var(--gold)"/>
      <polygon points="470,469 700,275 700,301 501,469" fill="var(--white)"/>
    </svg>
    <div class="brand">
      <div class="brand__name"><span class="brand__mark"></span>VERIDAX</div>
      <div class="brand__tagline">Luxury Landscapes</div>
    </div>
    <div class="person">
      <div class="person__name">Calvin Ostrow</div>
      <div class="person__role">Co-Founder / Project Manager</div>
      <div class="person__rule"></div>
      <div class="contacts">
        <div class="contacts__col">
          <div class="contact">
            <svg viewBox="0 0 16 16"><path d="M3 1l3 3-2 2c1 2 3 4 5 5l2-2 3 3-2 3C7 15 1 9 1 3z" fill="var(--gold)"/></svg>
            416-555-0193
          </div>
          <div class="contact">
            <svg viewBox="0 0 16 16"><rect x="4" y="1" width="8" height="14" rx="1.5" fill="none" stroke="var(--gold)" stroke-width="1.5"/><circle cx="8" cy="12.5" r="1" fill="var(--gold)"/></svg>
            416-555-0147
          </div>
        </div>
        <div class="contacts__col">
          <div class="contact">
            <svg viewBox="0 0 16 16"><rect x="1" y="3" width="14" height="10" fill="none" stroke="var(--gold)" stroke-width="1.5"/><path d="M1 3l7 6 7-6" fill="none" stroke="var(--gold)" stroke-width="1.5"/></svg>
            Calvin@veridax.ca
          </div>
          <div class="contact">
            <svg viewBox="0 0 16 16"><circle cx="8" cy="8" r="6.5" fill="none" stroke="var(--gold)" stroke-width="1.4"/><ellipse cx="8" cy="8" rx="3" ry="6.5" fill="none" stroke="var(--gold)" stroke-width="1.2"/><path d="M1.5 8h13" stroke="var(--gold)" stroke-width="1.2"/></svg>
            VERIDAX.CA
          </div>
        </div>
      </div>
    </div>
  </section>

</body>
</html>
```